Quillrun Couriers Web design

Take a look at our existing website(www.qlnrun.com) and design a new one, plus coding and recreate an existing logo.

```html
<!DOCTYPE html>
<html lang="en">
<head>
<meta charset="utf-8">
<title>Quillrun Couriers</title>
<link href="https://fonts.googleapis.com/css2?family=Lato:ital,wght@0,400;0,700;0,900;1,400&display=swap" rel="stylesheet">
<style>
:root{
  --navy:#0d3680;
  --blue:#0b4ea6;
  --deep:#0a2f78;
  --orange:#f1560f;
  --ink:#333;
  --muted:#555;
  --light:#f0f0f0;
  --white:#fff;
}
*{box-sizing:border-box;margin:0;padding:0}
html,body{width:1200px;height:3569px;overflow:hidden}
body{font-family:'Lato',sans-serif;color:var(--ink);background:var(--white);position:relative}
.abs{position:absolute}
.btn{display:inline-block;background:var(--orange);color:var(--white);font-weight:700;text-align:center;border-radius:2px}
.brand{font-weight:900;color:var(--navy);font-size:26px;letter-spacing:.5px;display:flex;align-items:center;gap:10px;line-height:1.05}
.brand .dot{width:14px;height:14px;background:var(--orange);border-radius:50%;flex:none}
.brand small{display:block;font-size:26px}

/* header */
.header{top:0;left:0;width:1200px;height:122px}
.header .brand{position:absolute;left:76px;top:40px}
.contact-top{position:absolute;right:68px;top:48px;display:flex;align-items:center;gap:26px;font-size:19px;font-weight:700;color:var(--navy)}
.contact-top span{display:flex;align-items:center;gap:10px}
.login{padding:9px 26px;font-size:17px;font-weight:400}
.nav{top:122px;left:0;width:1200px;height:47px;background:var(--navy);display:flex;justify-content:center;gap:58px;align-items:center}
.nav a{color:var(--white);text-decoration:none;font-size:17px;font-weight:700;letter-spacing:.3px}

/* hero */
.hero{top:169px;left:0;width:1200px;height:663px;background:linear-gradient(100deg,#4a3a2c 0%,#8a6a48 35%,#3553a6 65%,#2c4f9e 100%)}
.hero-text{position:absolute;top:200px;width:100%;text-align:center;color:var(--white)}
.hero-text h1{font-size:70px;font-weight:900;line-height:1}
.hero-text p{font-size:32px;margin-top:18px;line-height:1.4}
.hero-text .btn{margin-top:30px;width:182px;padding:8px 0;font-size:18px;font-weight:400}
.dots{position:absolute;top:612px;left:560px;display:flex;gap:12px}
.dots i{width:11px;height:11px;border-radius:50%;background:var(--white)}
.dots i:first-child{background:#1e78d8}

/* welcome */
.welcome-img{left:76px;top:898px;width:512px;height:398px;background:linear-gradient(135deg,#e8e9ea,#bfc3c8 55%,#7c6048)}
.welcome{left:615px;top:926px;width:515px}
.h2{font-size:30px;font-weight:900;color:var(--navy);line-height:1.2}
.h2 b{color:var(--blue);font-weight:900}
.welcome p{font-size:16.5px;line-height:30.5px;color:var(--muted);margin-top:20px}
.welcome .btn{margin-top:26px;width:151px;padding:10px 0;font-size:17px}

/* services */
.services-band{top:1373px;left:0;width:1200px;height:308px;background:linear-gradient(180deg,#1b2a55,#243a78)}
.services-title{top:1426px;width:1200px;text-align:center;color:var(--white);font-size:30px;font-weight:900}
.cards{top:1494px;left:283px;display:flex;gap:19px}
.card{width:199px;height:281px;background:var(--white);box-shadow:0 2px 8px rgba(0,0,0,.15);text-align:center;padding-top:26px}
.card h3{color:var(--orange);font-size:22px;font-weight:900;line-height:24px;margin-top:18px}
.card p{font-size:13.5px;line-height:19.5px;color:var(--ink);margin-top:14px;padding:0 12px}
.arrow{top:1618px}

/* testimonials */
.testimonials{top:1845px;left:0;width:1200px;height:355px;background:var(--light)}
.test-title{left:76px;top:1896px}
.quotes{top:1965px;left:76px;display:flex;gap:24px}
.quote{width:336px;display:flex;gap:18px}
.quote p{font-style:italic;font-size:14.5px;line-height:27.8px;color:var(--muted)}
.quote cite{display:block;font-style:normal;font-weight:700;color:var(--blue);font-size:14.5px;margin-top:8px}

/* benefits */
.benefits{left:76px;top:2280px}
.benefits ul{list-style:none;margin-top:28px}
.benefits li{display:flex;gap:17px;font-size:16.5px;line-height:25px;color:var(--ink);margin-bottom:14px;width:430px}
.benefits li svg{flex:none;margin-top:5px}
.benefits .btn{margin-top:30px;width:151px;padding:10px 0;font-size:17px}
.frame{left:614px;top:2240px;width:512px;height:452px;background:var(--orange)}
.benefit-img{left:580px;top:2267px;width:512px;height:398px;background:linear-gradient(100deg,#cfd8e2,#2f4f9a 30%,#3b4049 55%,#8b5a2e 85%,#c07a3a)}

/* contact */
.contact{top:2735px;left:0;width:1200px;height:475px;background:linear-gradient(90deg,#0f2f74,#143d95 40%,#123887)}
.contact h2{position:absolute;top:82px;width:100%;text-align:center;color:var(--white);font-size:30px;font-weight:900}
.form{position:absolute;top:132px;left:263px;display:grid;grid-template-columns:332px 332px;gap:10px 14px}
.field{height:44px;background:var(--white);border:1px solid #ccc;font-size:14.5px;color:#333;padding:14px 10px}
.submit{position:absolute;top:353px;left:434px;width:332px;height:44px;line-height:44px;font-size:17px}

/* footer */
.footer .brand{left:76px;top:3320px;font-size:22px}
.footer .brand small{font-size:22px}
.copy{left:76px;top:3398px;font-size:12px;line-height:22px;color:var(--ink)}
.fcol h4{font-size:15px;font-weight:700;color:var(--ink);letter-spacing:.3px}
.fnav{left:344px;top:3255px}
.fnav a{display:block;font-size:15px;color:var(--ink);text-decoration:none;margin-top:13.5px}
.fcontact{left:561px;top:3255px;font-size:13px;color:var(--ink)}
.fcontact .name{color:var(--orange);font-size:15.5px;font-weight:400;margin-top:18px}
.fcontact .row{display:flex;align-items:center;gap:18px;margin-top:10px}
.fcontact .row span{line-height:18px}
.fsub{left:884px;top:3250px}
.subscribe{display:flex;margin-top:18px}
.subscribe div{width:200px;height:40px;background:#eee;font-size:13px;padding:13px 10px;color:#333}
.subscribe .go{width:42px;background:var(--orange);color:var(--white);font-weight:700;font-size:14px;padding:12px 0;text-align:center}
.social{display:flex;gap:20px;margin-top:22px}
.social i{width:22px;height:22px;border-radius:50%;background:var(--navy)}
</style>
</head>
<body>

<header class="header abs">
  <div class="brand"><span class="dot"></span><span>QUILLRUN<small>COURIERS</small></span></div>
  <div class="contact-top">
    <span><svg width="16" height="16" viewBox="0 0 24 24"><path fill="#0d3680" d="M6.6 10.8a15 15 0 006.6 6.6l2.2-2.2c.3-.3.7-.4 1-.2 1.1.4 2.3.6 3.6.6.6 0 1 .4 1 1V20c0 .6-.4 1-1 1A17 17 0 013 4c0-.6.4-1 1-1h3.5c.6 0 1 .4 1 1 0 1.3.2 2.5.6 3.6.1.3 0 .7-.2 1z"/></svg>555-310-7170</span>
    <span><svg width="18" height="14" viewBox="0 0 18 14"><rect width="18" height="14" rx="1" fill="#0d3680"/><path d="M1 1l8 6 8-6" stroke="#fff" stroke-width="1.6" fill="none"/></svg><span style="font-weight:400">info@qlnrun.com</span></span>
    <a class="btn login">LOG IN</a>
  </div>
</header>

<nav class="nav abs">
  <a>HOME</a><a>ABOUT US</a><a>SERVICES</a><a>RATES</a><a>CUSTOMER BENEFITS</a><a>LOGISTICS</a><a>CONTACT US</a>
</nav>

<section class="hero abs" role="img" aria-label="Smiling courier in blue uniform holding a cardboard parcel beside a van full of boxes">
  <div class="hero-text">
    <h1>Quillrun Couriers</h1>
    <p>Sed ut perspiciatis unde omnis iste natus error<br>sit voluptatem accusantium.</p>
    <a class="btn">Read More</a>
  </div>
  <div class="dots"><i></i><i></i><i></i><i></i></div>
</section>

<div class="welcome-img abs" role="img" aria-label="Two movers in overalls standing beside a white delivery van loaded with boxes"></div>
<section class="welcome abs">
  <h2 class="h2">WELCOME TO<br><b>QUILLRUN COURIERS</b></h2>
  <p>We are committed to providing professional messenger services to cater for the most important, emergency and time sensitive deliveries valuable to your company. Our services range from scheduled local and long distance, same day to all types of On Demand services. Our goal is to become a leader by showing reliability, integrity as well as competitive pricing.</p>
  <a class="btn">Read More</a>
</section>

<div class="services-band abs" role="img" aria-label="Delivery van at dusk in dark blue tones"></div>
<h2 class="services-title abs">OUR SERVICES</h2>
<svg class="arrow abs" style="left:244px" width="16" height="28" viewBox="0 0 16 28"><path d="M13 3L3 14l10 11" stroke="#fff" stroke-width="3" fill="none"/></svg>
<svg class="arrow abs" style="left:938px" width="16" height="28" viewBox="0 0 16 28"><path d="M3 3l10 11L3 25" stroke="#fff" stroke-width="3" fill="none"/></svg>
<div class="cards abs">
  <div class="card">
    <svg width="52" height="62" viewBox="0 0 52 62"><rect x="4" y="8" width="44" height="52" fill="none" stroke="#0b4ea6" stroke-width="4"/><path d="M22 2h8v6h6v8h-6v6h-8v-6h-6V8h6z" fill="#0b4ea6"/><g fill="#0b4ea6"><rect x="12" y="28" width="7" height="7"/><rect x="22" y="28" width="7" height="7"/><rect x="32" y="28" width="7" height="7"/><rect x="12" y="40" width="7" height="7"/><rect x="32" y="40" width="7" height="7"/><rect x="22" y="44" width="8" height="16"/></g></svg>
    <h3>Hospital &amp;<br>Medical Care</h3>
    <p>Hospital &amp; Medical Care Home Deliveries, Pharmaceuticals and Critical Routes...</p>
  </div>
  <div class="card">
    <svg width="54" height="62" viewBox="0 0 54 62"><rect x="2" y="2" width="50" height="58" rx="5" fill="#0b4ea6"/><rect x="9" y="9" width="36" height="13" fill="#fff"/><g fill="#fff"><rect x="9" y="28" width="9" height="8"/><rect x="22" y="28" width="9" height="8"/><rect x="35" y="28" width="9" height="8"/><rect x="9" y="42" width="9" height="8"/><rect x="22" y="42" width="9" height="8"/><rect x="35" y="42" width="9" height="12"/></g></svg>
    <h3>Banking<br>&amp; Brokerage</h3>
    <p>Banking &amp; Brokerage Emergency Deliveries, Mortgage Documents, Interoffice Routes ...</p>
  </div>
  <div class="card">
    <svg width="48" height="62" viewBox="0 0 48 62"><path d="M4 4h26l14 14v40H4z" fill="none" stroke="#0b4ea6" stroke-width="4"/><path d="M30 4v14h14" fill="none" stroke="#0b4ea6" stroke-width="4"/><g stroke="#0b4ea6" stroke-width="4"><path d="M12 30h24M12 39h24M12 48h24"/></g></svg>
    <h3>Legal<br>Filings</h3>
    <p>Legal, Administrative and also deliveries associated with Manufacturing. ...</p>
  </div>
</div>

<section class="testimonials abs"></section>
<h2 class="h2 test-title abs">WHAT PEOPLE <b>ARE SAYING?</b></h2>
<svg class="abs" style="left:1072px;top:1893px" width="48" height="22" viewBox="0 0 48 22"><path d="M10 2L2 11l8 9M38 2l8 9-8 9" stroke="#888" stroke-width="2.5" fill="none"/></svg>
<div class="quotes abs">
  <div class="quote"><svg width="28" height="24" viewBox="0 0 28 24" style="flex:none"><path d="M0 24V12C0 5 4 1 11 0v4c-4 1-6 3-6 7h6v13zM16 24V12c0-7 4-11 11-12v4c-4 1-6 3-6 7h6v13z" fill="#f1560f"/></svg><div><p>Aliquam molestie, mi et imperdiet euismod, dui purus auctor tellus, et interdum lacus lectus et ante. Sed accumsan sollicitudin sapien, sit amet adipiscing turpis gravida ac In congue, neque ac lobortis....”</p><cite>-Name Heading</cite></div></div>
  <div class="quote"><svg width="28" height="24" viewBox="0 0 28 24" style="flex:none"><path d="M0 24V12C0 5 4 1 11 0v4c-4 1-6 3-6 7h6v13zM16 24V12c0-7 4-11 11-12v4c-4 1-6 3-6 7h6v13z" fill="#f1560f"/></svg><div><p>Aliquam molestie, mi et imperdiet euismod, dui purus auctor tellus, et interdum lacus lectus et ante. Sed accumsan sollicitudin sapien, sit amet adipiscing turpis gravida ac In congue, neque ac lobortis....”</p><cite>-Name Heading</cite></div></div>
  <div class="quote"><svg width="28" height="24" viewBox="0 0 28 24" style="flex:none"><path d="M0 24V12C0 5 4 1 11 0v4c-4 1-6 3-6 7h6v13zM16 24V12c0-7 4-11 11-12v4c-4 1-6 3-6 7h6v13z" fill="#f1560f"/></svg><div><p>Aliquam molestie, mi et imperdiet euismod, dui purus auctor tellus, et interdum lacus lectus et ante. Sed accumsan sollicitudin sapien, sit amet adipiscing turpis gravida ac In congue, neque ac lobortis....”</p><cite>-Name Heading</cite></div></div>
</div>

<section class="benefits abs">
  <h2 class="h2">CUSTOMER <b>BENEFITS</b></h2>
  <ul>
    <li><svg width="17" height="17" viewBox="0 0 17 17"><circle cx="8.5" cy="8.5" r="7.5" fill="none" stroke="#0d3680" stroke-width="1.5"/><path d="M5 8.7l2.4 2.4L12 6.5" stroke="#0d3680" stroke-width="1.6" fill="none"/></svg>Money back guaranteed if your package is not delivered on time</li>
    <li><svg width="17" height="17" viewBox="0 0 17 17"><circle cx="8.5" cy="8.5" r="7.5" fill="none" stroke="#0d3680" stroke-width="1.5"/><path d="M5 8.7l2.4 2.4L12 6.5" stroke="#0d3680" stroke-width="1.6" fill="none"/></svg>Free waiting time</li>
    <li><svg width="17" height="17" viewBox="0 0 17 17"><circle cx="8.5" cy="8.5" r="7.5" fill="none" stroke="#0d3680" stroke-width="1.5"/><path d="M5 8.7l2.4 2.4L12 6.5" stroke="#0d3680" stroke-width="1.6" fill="none"/></svg>All our services are guaranteed</li>
    <li><svg width="17" height="17" viewBox="0 0 17 17"><circle cx="8.5" cy="8.5" r="7.5" fill="none" stroke="#0d3680" stroke-width="1.5"/><path d="M5 8.7l2.4 2.4L12 6.5" stroke="#0d3680" stroke-width="1.6" fill="none"/></svg>Pickup within 15 to 30 mins.of your call or sooner</li>
    <li><svg width="17" height="17" viewBox="0 0 17 17"><circle cx="8.5" cy="8.5" r="7.5" fill="none" stroke="#0d3680" stroke-width="1.5"/><path d="M5 8.7l2.4 2.4L12 6.5" stroke="#0d3680" stroke-width="1.6" fill="none"/></svg>First 100lbs. are free</li>
    <li><svg width="17" height="17" viewBox="0 0 17 17"><circle cx="8.5" cy="8.5" r="7.5" fill="none" stroke="#0d3680" stroke-width="1.5"/><path d="M5 8.7l2.4 2.4L12 6.5" stroke="#0d3680" stroke-width="1.6" fill="none"/></svg>State of the art courier software system</li>
  </ul>
  <a class="btn">Read More</a>
</section>
<div class="frame abs"></div>
<div class="benefit-img abs" role="img" aria-label="Courier in blue cap handing a parcel to a customer at her front door"></div>

<section class="contact abs" role="img" aria-label="Blue-tinted courier van background">
  <h2>QUICK CONTACT</h2>
  <div class="form">
    <div class="field">*Full Name:</div><div class="field">*Zip Code:</div>
    <div class="field">*Street Address:</div><div class="field">*Email:</div>
    <div class="field">*City Or Town:</div><div class="field">*Phone:</div>
    <div class="field">*State:</div><div class="field">*Regarding</div>
  </div>
  <a class="btn submit">Submit Now</a>
</section>

<footer class="footer">
  <div class="brand abs"><span class="dot"></span><span>QUILLRUN<small>COURIERS</small></span></div>
  <p class="copy abs">Copyright © 2021. Company Name.<br>All Right Reserved</p>
  <div class="fcol fnav abs">
    <h4>NAVIGATION</h4>
    <a>Home</a><a>About Us</a><a>Services</a><a>Rates</a><a>Customer Benefits</a><a>Logistics</a><a>Contact Us</a>
  </div>
  <div class="fcol fcontact abs">
    <h4>CONTACT INFO</h4>
    <div class="name">Quillrun Couriers</div>
    <div style="margin-top:8px">412 Harbor Lane, Milltown, NY 10000</div>
    <div class="name">Quillrun Couriers</div>
    <div style="margin-top:6px">P.O. Box 5120 Riverton, NY 10010</div>
    <div class="row"><svg width="12" height="12" viewBox="0 0 24 24"><path fill="#333" d="M6.6 10.8a15 15 0 006.6 6.6l2.2-2.2c.3-.3.7-.4 1-.2 1.1.4 2.3.6 3.6.6.6 0 1 .4 1 1V20c0 .6-.4 1-1 1A17 17 0 013 4c0-.6.4-1 1-1h3.5c.6 0 1 .4 1 1 0 1.3.2 2.5.6 3.6.1.3 0 .7-.2 1z"/></svg><span>555-310-7170,&nbsp;&nbsp; 555-310-2427</span></div>
    <div class="row"><svg width="12" height="12" viewBox="0 0 12 12"><rect x="1" y="4" width="10" height="7" fill="#333"/><rect x="3" y="1" width="6" height="4" fill="#333"/></svg><span>555-310-7041</span></div>
    <div class="row"><svg width="12" height="10" viewBox="0 0 12 10"><rect width="12" height="10" fill="#333"/><path d="M1 1l5 4 5-4" stroke="#fff" fill="none"/></svg><span>info@qlnrun.com</span></div>
  </div>
  <div class="fcol fsub abs">
    <h4>EMAIL SUBSCRIBE</h4>
    <div class="subscribe"><div>Enter Email Address</div><div class="go">GO</div></div>
    <h4 style="margin-top:36px">FOLLOW US</h4>
    <div class="social"><i></i><i></i><i></i><i></i><i></i></div>
  </div>
</footer>

</body>
</html>
```